A Lantern at Dawn

A story of the first year of life of our son who was born with a birth defect. A journey of a family that was shocked and overwhelmed by the fear of the unknown future and perils of surgeries and treatments that would be required. A story written by the dad about how he and his wife coped with and overcame adversity with hope, perseverance and through learning about what would be required to have a normal and bright future for their child by bravely advocating for nothing but the best medical and functional outcome for their child. The story is a detailed version of the medical aspects (Surgeries, recoveries, infections, treatment regimens, a less than ideal medical system) as well as the psychosocial aspects (Taking time off work, mental burden due to excessive worry, financial hardships, challenges with an unfriendly insurance system) of life as they went through this challenging journey. The book gives a realistic account for what to expect when such a situation arises, but also gives valuable tips and suggestions on dos and don’ts so that others may benefit from the author’s experience. The epilogue takes about how our son is doing very well now (15 years old). The title reflects about the occurrence of this birth defect - one in 5000 babies born have this rare birth defect.

Book chapter names to help you get a synopsis of the story: Chapter 1: Anticipation of new life · Chapter 2: Shock and Joy · Chapter 3: Intro to NICU · Chapter 4: The Diagnosis · Chapter 5: In Denial · Chapter 6: Coming to terms · Chapter 7: Sunday: anything but a fun day · Chapter 8: Long overdue · Chapter 9: The Colostomy · Chapter 10: The Complication · Chapter 11: The Diary of the first month · Chapter 12: Trouble doubled · Chapter 13: The new normal · Chapter 14: Small glimmers of hope · Chapter 15: Improvement momentum · Chapter 16: Homecoming · Chapter 17: Settling in · Chapter 18: Readmission · Chapter 19: Going to New York · Chapter 20: Baby on board · Chapter 21: Snowy Touchdown · Chapter 22: The Appointment · Chapter 23: Moving Forward · Chapter 24: The Road trip · Chapter 25: Goodbye · Chapter 26: Preparing for the next surgery · Chapter 27: On the road again · Chapter 28: Home away from Home · Chapter 29: The PSARP Operation · Chapter 30: Sigh of relief · Chapter 31: Recovery · Chapter 32: Things going right · Chapter 33: Blissful Healing · Chapter 34: Post-Op recovery at QLV · Chapter 35: Déjà vu: Homecoming 2 · Chapter 36: The Insurance Aftermath · Chapter 37: Building confidence · Chapter 38: Better preparation · Chapter 39: Help from Grandparents · Chapter 40: Hello Cincinnati! · Chapter 41: The Promise of a Better Tomorrow · Chapter 42: The closure (of the colostomy) · Chapter 43: The Beautiful News of a successful Surgery · Chapter 44: Changing the Outcome Together · Chapter 45: Experiencing “Normal” · Chapter 46: Smooth Recovery · Chapter 47: All’s well that ends well

Target Market(s)

Health care professionals, parents of children with chronic medical conditions, people interested in patient family experience improvement

Industry/Entity Type

Healthcare

Requirements
Must have
• Journey, roadmap, baby, healthcare
Nice to have
• Realism about difficulties in dealing with chronic medical conditions but also inspiration to learn and overcome adversity. Should provoke curiosity and empathy and a desire to learn about the story of the baby that bear the odds and had a good outcome. A beacon of hope!
Should not have
• Should not be generic,

```html
<!DOCTYPE html>
<html lang="en">
<head>
<meta charset="utf-8">
<title>A Lantern at Dawn — Book Cover</title>
<link href="https://fonts.googleapis.com/css2?family=Anton&family=Playfair+Display+SC:wght@400&display=swap" rel="stylesheet">
<style>
  :root {
    --page-bg: #e8e8e8;
    --night: #1b2628;
    --deep-teal: #1f4f55;
    --teal: #2e7a80;
    --haze: #a9c2bb;
    --dusk-pale: #d8c9a8;
    --ember: #e2763a;
    --ember-deep: #b9482a;
    --ground: #1f2423;
    --title-ink: #dde4d3;
    --author-ink: #f3f1ea;
  }
  * { margin: 0; padding: 0; box-sizing: border-box; }
  html, body {
    width: 1200px; height: 999px; overflow: hidden;
    background: var(--page-bg);
  }
  .cover {
    position: absolute;
    left: 296px; top: 30px;
    width: 608px; height: 940px;
    background: var(--ground);
    overflow: hidden;
  }
  .cover-art {
    position: absolute; left: 0; top: 0;
    width: 100%; height: 680px;
    background: linear-gradient(to bottom,
      var(--night) 0%,
      var(--deep-teal) 20%,
      var(--teal) 40%,
      var(--haze) 62%,
      var(--dusk-pale) 72%,
      var(--ember) 83%,
      var(--ember-deep) 90%,
      var(--ground) 100%);
  }
  .author {
    position: absolute; top: 20px; left: 0; width: 100%;
    text-align: center;
    font-family: "Playfair Display SC", serif;
    font-size: 36px; letter-spacing: 0.5px;
    color: var(--author-ink);
  }
  .book-title { font-weight: 400; }
  .title {
    position: absolute; left: 0; width: 100%;
    font-family: "Anton", sans-serif;
    color: var(--title-ink);
    text-transform: uppercase;
    line-height: 1;
    white-space: nowrap;
  }
  .title-lead { top: 604px; left: 68px; width: auto; font-size: 40px; letter-spacing: 1px; }
  .title-main { top: 646px; text-align: center; font-size: 135px; letter-spacing: 6px; padding-left: 36px; }
  .title-tail { top: 779px; text-align: center; font-size: 102px; letter-spacing: 3px; padding-left: 34px; }
</style>
</head>
<body>
  <main class="cover">
    <div class="cover-art" role="img" aria-label="Cover illustration: dusk sky scene"></div>
    <p class="author">Marin Tallis</p>
    <h1 class="book-title">
      <span class="title title-lead">A</span>
      <span class="title title-main">Lantern</span>
      <span class="title title-tail">at Dawn</span>
    </h1>
  </main>
</body>
</html>
```